Website for company called VORENTbio

We need a website for our new company called VORENTbio which developed a platform/technology to identify antigen-specific T cells (immune cells) which can be used for cancer therapy, autoimmunity, etc.

The platform is called VORENT and is rapid, versatile, unbiased, and inexpensive.

We have a semi-final logo although we are not completely set on color and font of text (attached).

Target Market(s)

Our target audience at the moment would be potential investors and VCs. We eventually are interested in getting attention from scientists and cell/immunotherapy companies.

Industry/Entity Type

Healthcare/Technology

Coding

Coded - Design and coding required

Number of Pages Required

1 page

Colors
0094D4
00A9DD
6FCCEA
C7EBF8
E9F6FB
00AB8E
00BBA5
67D7C9
C6EFE9
E9F9F6
E54698
E96AAD
F1A4CE
F9D9EA
FCEFF6
A7469A
B969AE
D3A5CF
EDDBEB
F8F0F9
6B429C
8869AF
B7A5CE
E3DAEB
F3F0F8

Requirements
Must have
• Landing page about the company, About us page, Technology page (could be merged with company landing page), Contact us page

```html
<!DOCTYPE html>
<html lang="en">
<head>
<meta charset="utf-8">
<title>VORENTbio — Antigen-Specific T Cells</title>
<link href="https://fonts.googleapis.com/css2?family=Poppins:wght@400;500;600;700&display=swap" rel="stylesheet">
<style>
:root{
  --ink:#0f1240;
  --body:#55586e;
  --primary:#3535ee;
  --lav:#f1f0fd;
  --lav-2:#e4e2fb;
  --footer:#0b0c36;
  --line:#e3e3ef;
  --white:#ffffff;
  --star:#f5b42a;
  --photo-a:#dfe6ee;
  --photo-b:#b9c7d6;
}
*{box-sizing:border-box;margin:0;padding:0}
html,body{width:1200px;height:3496px;overflow:hidden}
body{font-family:"Poppins",sans-serif;color:var(--body);background:var(--white);position:relative;font-size:13px;line-height:1.6}
.abs{position:absolute}
h1,h2,h3,h4{color:var(--ink);font-weight:700;line-height:1.15}
.btn{display:inline-block;padding:12px 24px;border-radius:6px;font-size:12px;font-weight:600;text-decoration:none;line-height:1.4;white-space:nowrap}
.btn-primary{background:var(--primary);color:var(--white)}
.btn-outline{border:1.5px solid var(--ink);color:var(--ink);background:var(--white)}
.photo{background:linear-gradient(135deg,var(--photo-a),var(--photo-b))}
.link-more{color:var(--primary);font-size:11px;font-weight:600}
.stack{display:flex;flex-direction:column;align-items:flex-start}

/* nav */
.nav{top:0;left:120px;width:960px;height:80px;z-index:5;display:flex;align-items:center;justify-content:space-between}
.brand{display:flex;align-items:center;gap:8px;font-size:22px;font-weight:700;color:var(--ink)}
.brand-dot{width:20px;height:20px;border-radius:50%;background:var(--ink)}
.nav-right{display:flex;align-items:center;gap:34px}
.nav-links{display:flex;gap:24px;font-size:12px;color:var(--ink);font-weight:500}
.nav-links .active{color:var(--primary);border-bottom:2px solid var(--primary)}
.nav-cta{padding:9px 22px}

/* hero */
.hero{top:0;left:0;width:1200px;height:600px;background:linear-gradient(90deg,#fbfcfe 0%,#f1f4f8 55%,#e7ecf2 100%)}
.hero-photo{left:640px;top:0;width:560px;height:600px;background:linear-gradient(160deg,#eef2f6,#c9d5e1 60%,#dce3eb)}
.hero-copy{left:120px;top:104px;width:520px;gap:0}
.hero-copy h1{font-size:50px;margin-bottom:16px}
.hero-text{width:440px;font-size:12px;margin-bottom:20px}
.hero-btns{display:flex;gap:14px}
.hero-cards{left:120px;top:452px;display:flex;gap:30px}
.hero-card{height:120px;background:var(--white);border-radius:10px;box-shadow:0 8px 24px rgba(20,20,80,.08);display:flex;padding:16px;gap:12px}
.hero-card h4{font-size:16px;width:110px}
.hero-card .thumb{width:110px;height:88px;border-radius:8px}
.hero-card.wide{width:340px}
.hero-card.wide h4{width:160px}

/* what we do */
.what{top:600px;left:0;width:1200px;height:500px;background:var(--white)}
.what-ring{left:110px;top:60px}
.what-photo{left:160px;top:110px;width:300px;height:300px;border-radius:50%}
.what-copy{left:680px;top:110px;width:400px}
.what-copy h2{font-size:38px;margin-bottom:16px}
.what-copy p{margin-bottom:12px;font-size:12px}
.what-copy .btn{margin-top:8px;padding:9px 20px}

/* advantage */
.adv{top:1100px;left:0;width:1200px;height:380px;background:var(--lav)}
.sec-title{width:1200px;text-align:center;font-size:34px}
.adv .sec-title{top:44px;left:0}
.adv-cards{left:120px;top:126px;display:flex;gap:20px}
.adv-card{width:225px;height:110px;background:var(--white);border-radius:10px;padding:16px;display:flex;gap:12px}
.adv-icon{width:36px;height:36px;border-radius:8px;border:1.5px solid var(--primary);flex-shrink:0;display:flex;align-items:center;justify-content:center}
.adv-card h4{font-size:15px;margin-bottom:4px}
.adv-card p{font-size:10px;line-height:1.45;margin-bottom:4px}
.arrow{width:30px;height:30px;border-radius:50%;background:var(--white);border:1px solid var(--line);display:flex;align-items:center;justify-content:center}
.adv .btn{left:525px;top:288px;padding:10px 22px;font-size:11px}

/* therapy */
.ther{top:1480px;left:0;width:1200px;height:560px}
.ther .sec-title{top:44px;left:0}
.ther-cards{left:120px;top:128px;display:flex;gap:40px}
.ther-card{width:306px}
.ther-card .photo{height:196px;border-radius:10px;margin-bottom:16px}
.ther-card h3{font-size:19px;margin-bottom:6px}
.ther-card p{font-size:11px;line-height:1.5;margin-bottom:4px}
.ther .btn{left:530px;top:480px;padding:10px 22px;font-size:11px}

/* business */
.biz{top:2040px;left:0;width:1200px;height:500px;background:linear-gradient(90deg,#efedff 0%,#e4e1fb 60%,#d9d5f8 100%)}
.biz-copy{left:120px;top:96px;width:460px}
.biz-copy h2{font-size:42px;margin-bottom:20px}
.biz-text{font-size:12px;margin-bottom:24px}
.biz-btns{display:flex;gap:14px}
.biz-ring{left:740px;top:40px}
.biz-photo{left:790px;top:90px;width:320px;height:320px;border-radius:50%}

/* reviews */
.rev{top:2540px;left:0;width:1200px;height:420px}
.rev .sec-title{top:48px;left:0}
.rev-cols{left:120px;top:130px;display:flex;gap:80px}
.rev-item{width:440px}
.quote{font-size:64px;line-height:.7;color:var(--lav-2);font-weight:700;margin-bottom:6px}
.rev-item blockquote{font-size:19px;line-height:1.4;color:var(--ink);font-weight:500;margin-bottom:20px}
.rev-person{display:flex;gap:12px;align-items:center}
.avatar{width:44px;height:44px;border-radius:50%}
.stars{color:var(--star);font-size:12px;letter-spacing:1px}
.rev-person p{font-size:10px;line-height:1.4}

/* talk */
.talk{top:2960px;left:0;width:1200px;height:240px;background:linear-gradient(90deg,#6262f0,#7c7cf5)}
.talk-photo{left:120px;top:0;width:420px;height:240px;background:linear-gradient(135deg,#c7d3e6,#98a9c8)}
.talk-copy{left:700px;top:44px;width:380px}
.talk-copy h2{color:var(--white);font-size:38px;margin-bottom:10px}
.talk-copy p{color:#e8e8ff;font-size:11px;margin-bottom:16px}
.talk-copy .btn{background:var(--white);color:var(--ink);padding:10px 22px}

/* footer */
.foot{top:3200px;left:0;width:1200px;height:296px;background:var(--footer);color:#b8bad6}
.foot-brand{left:120px;top:36px;display:flex;align-items:center;gap:8px;color:var(--white);font-size:22px;font-weight:700}
.foot-brand .brand-dot{background:var(--white)}
.foot-about{left:120px;top:84px;width:270px;font-size:10px;line-height:1.55}
.foot h4{color:var(--white);font-size:15px;margin-bottom:14px}
.foot ul{list-style:none;font-size:10px}
.foot li{margin-bottom:8px;display:flex;align-items:center;gap:8px}
.ficon{width:18px;height:18px;border-radius:50%;background:#2a2c66;flex-shrink:0}
.col-links{left:430px;top:42px}
.col-contact{left:580px;top:42px}
.col-follow{left:780px;top:42px}
.col-news{left:900px;top:42px;width:180px}
.news-input{height:34px;border-radius:5px;background:var(--white);color:#888;font-size:10px;padding:9px 10px;margin-bottom:10px}
.news-btn{height:34px;border-radius:5px;background:var(--primary);color:var(--white);font-size:11px;font-weight:600;text-align:center;padding-top:8px}
.foot-bottom{left:120px;top:252px;width:960px;border-top:1px solid #26285a;padding-top:14px;display:flex;justify-content:space-between;font-size:10px}
.foot-bottom span+span{margin-left:22px}
</style>
</head>
<body>

<section class="hero abs">
  <div class="hero-photo abs" role="img" aria-label="Smiling female doctor in a white coat with a stethoscope, standing in a bright lab"></div>
  <div class="hero-copy stack abs">
    <h1>Unlocking the Power of Antige -Specific T Cells</h1>
    <p class="hero-text">VORENTbio is pioneering a novel platform to rapidly and precisely identify the T cells that drive effective cancer immunotherapy.</p>
    <div class="hero-btns">
      <a class="btn btn-primary" href="#">Download Investor Brief</a>
      <a class="btn btn-outline" href="#">Contact The Team</a>
    </div>
  </div>
  <div class="hero-cards abs">
    <div class="hero-card"><h4>Patients and caregivers</h4><div class="thumb photo" role="img" aria-label="Patient talking with a caregiver"></div></div>
    <div class="hero-card"><h4>Patients and caregivers</h4><div class="thumb photo" role="img" aria-label="Clinician in a hospital setting"></div></div>
    <div class="hero-card wide"><h4>Scientists and researchers</h4><div class="thumb photo" role="img" aria-label="Research scientists in a laboratory"></div></div>
  </div>
</section>

<header class="nav abs">
  <div class="brand"><span class="brand-dot"></span>vorentbio</div>
  <div class="nav-right">
    <nav class="nav-links">
      <span class="active">Home</span><span>About Us</span><span>Stories</span><span>Advantage</span><span>Investors</span>
    </nav>
    <a class="btn btn-primary nav-cta" href="#">Contact Us</a>
  </div>
</header>

<section class="what abs">
  <svg class="what-ring abs" width="380" height="380" viewBox="0 0 380 380">
    <path d="M190 20 A170 170 0 0 1 360 190" fill="none" stroke="#3535ee" stroke-width="6" stroke-linecap="round"/>
    <circle cx="190" cy="190" r="170" fill="none" stroke="#e4e2fb" stroke-width="2"/>
  </svg>
  <div class="what-photo photo abs" role="img" aria-label="Doctor examining an elderly patient"></div>
  <div class="what-copy stack abs">
    <h2>What We Do</h2>
    <p>Immunotherapies have transformed cancer treatment — but finding the right T cells remains a major bottleneck. Existing methods are slow, expensive, and biased.</p>
    <p>VORENTbio has developed VORENT, a proprietary platform that rapidly identifies antigen-specific T cells — unlocking a faster, more accurate path to personalized and targeted cancer therapies.</p>
    <a class="btn btn-primary" href="#">Learn More</a>
  </div>
</section>

<section class="adv abs">
  <h2 class="sec-title abs">The VORENT Advantage</h2>
  <div class="arrow abs" style="left:76px;top:166px"><svg width="10" height="10" viewBox="0 0 10 10"><path d="M7 1 3 5l4 4" fill="none" stroke="#0f1240" stroke-width="1.6"/></svg></div>
  <div class="arrow abs" style="left:1094px;top:166px"><svg width="10" height="10" viewBox="0 0 10 10"><path d="M3 1l4 4-4 4" fill="none" stroke="#0f1240" stroke-width="1.6"/></svg></div>
  <div class="adv-cards abs">
    <div class="adv-card"><div class="adv-icon"><svg width="18" height="18" viewBox="0 0 18 18"><path d="M10 1 3 10h5l-1 7 7-9H9z" fill="none" stroke="#3535ee" stroke-width="1.5"/></svg></div><div><h4>Rapid</h4><p>Detect target-reactive T cells in under 48 hours</p><span class="link-more">Learn More</span></div></div>
    <div class="adv-card"><div class="adv-icon"><svg width="18" height="18" viewBox="0 0 18 18"><circle cx="9" cy="9" r="7" fill="none" stroke="#3535ee" stroke-width="1.5"/><circle cx="9" cy="9" r="2.5" fill="#3535ee"/></svg></div><div><h4>Unbiased</h4><p>No prior epitope or HLA knowledge required</p><span class="link-more">Learn More</span></div></div>
    <div class="adv-card"><div class="adv-icon"><svg width="18" height="18" viewBox="0 0 18 18"><path d="M2 15h14M4 12V8M9 12V4M14 12V6" fill="none" stroke="#3535ee" stroke-width="1.5"/></svg></div><div><h4>Scalable</h4><p>From early discovery to clinical pipeline</p><span class="link-more">Learn More</span></div></div>
    <div class="adv-card"><div class="adv-icon"><svg width="18" height="18" viewBox="0 0 18 18"><circle cx="9" cy="9" r="7" fill="none" stroke="#3535ee" stroke-width="1.5"/><path d="M9 4v10M11.5 6.5H8a1.5 1.5 0 0 0 0 3h2a1.5 1.5 0 0 1 0 3H6.5" fill="none" stroke="#3535ee" stroke-width="1.3"/></svg></div><div><h4>Cost-Effective</h4><p>Minimal infrastructure, maximum insight</p><span class="link-more">Learn More</span></div></div>
  </div>
  <a class="btn btn-outline abs" href="#">View All Advantage</a>
</section>

<section class="ther abs">
  <h2 class="sec-title abs">Enabling the Future of Cancer Immunotherapy</h2>
  <div class="arrow abs" style="left:76px;top:212px"><svg width="10" height="10" viewBox="0 0 10 10"><path d="M7 1 3 5l4 4" fill="none" stroke="#0f1240" stroke-width="1.6"/></svg></div>
  <div class="arrow abs" style="left:1094px;top:212px"><svg width="10" height="10" viewBox="0 0 10 10"><path d="M3 1l4 4-4 4" fill="none" stroke="#0f1240" stroke-width="1.6"/></svg></div>
  <div class="ther-cards abs">
    <div class="ther-card"><div class="photo" role="img" aria-label="Scientists working at a laboratory bench"></div><h3>Patient-Specific Targeting</h3><p>Match the right T cells to each individual's tumor signature.</p><span class="link-more">Learn More</span></div>
    <div class="ther-card"><div class="photo" role="img" aria-label="Patient entering an imaging scanner"></div><h3>TCR Discovery</h3><p>Accelerate the development of engineered T cell receptors.</p><span class="link-more">Learn More</span></div>
    <div class="ther-card"><div class="photo" role="img" aria-label="Doctor consulting with a patient"></div><h3>Monitoring &amp; Biomarkers</h3><p>Track immune response dynamics in real time.</p><span class="link-more">Learn More</span></div>
  </div>
  <a class="btn btn-outline abs" href="#">View All Therapy</a>
</section>

<section class="biz abs">
  <div class="biz-copy stack abs">
    <h2>Built for Science.<br>Ready for Business.</h2>
    <p class="biz-text">The global market for T cell–based immunotherapies is booming, yet T cell discovery tools haven't kept pace. With early proof-of-concept data and IP pending, VORENTbio is now seeking seed investment to scale development, validate with clinical collaborators, and bring the transformative platform to market.</p>
    <div class="biz-btns">
      <a class="btn btn-primary" href="#">Download Pitch Deck</a>
      <a class="btn btn-outline" href="#">Schedule a Call</a>
    </div>
  </div>
  <svg class="biz-ring abs" width="420" height="420" viewBox="0 0 420 420">
    <path d="M210 20 A190 190 0 0 0 20 210" fill="none" stroke="#3535ee" stroke-width="6" stroke-linecap="round"/>
    <circle cx="210" cy="210" r="190" fill="none" stroke="#ffffff" stroke-width="2" opacity=".7"/>
  </svg>
  <div class="biz-photo photo abs" role="img" aria-label="Elderly patient smiling while talking with a doctor"></div>
</section>

<section class="rev abs">
  <h2 class="sec-title abs">Customer review</h2>
  <div class="rev-cols abs">
    <div class="rev-item">
      <div class="quote">&ldquo;</div>
      <blockquote>"VORENT is a breakthrough in T cell discovery. We've used it to isolate rare tumor-reactive cells we couldn't detect with standard methods."</blockquote>
      <div class="rev-person"><div class="avatar photo" role="img" aria-label="Reviewer portrait"></div><div><div class="stars">★★★★★</div><p>Dr. Hana Lindqvist, Director of Immuno-Oncology,<br>Northfield Cancer Institute</p></div></div>
    </div>
    <div class="rev-item">
      <div class="quote">&ldquo;</div>
      <blockquote>"The speed and sensitivity of VORENT gives us a clear edge in identifying personalized T cell targets for our clinical pipeline."</blockquote>
      <div class="rev-person"><div class="avatar photo" role="img" aria-label="Reviewer portrait"></div><div><div class="stars">★★★★★</div><p>Dr. Tomas Reyna, CSO, Calder Therapeutics</p></div></div>
    </div>
  </div>
</section>

<section class="talk abs">
  <div class="talk-photo abs" role="img" aria-label="Team of medical professionals in scrubs and masks"></div>
  <div class="talk-copy stack abs">
    <h2>Let's Talk</h2>
    <p>Whether you're an investor, researcher, or strategic partner, we welcome collaboration. We'd love to share how VORENTbio can advance your immunotherapy pipeline.</p>
    <a class="btn" href="#">Get Started</a>
  </div>
</section>

<footer class="foot abs">
  <div class="foot-brand abs"><span class="brand-dot"></span>vorentbio</div>
  <p class="foot-about abs">VORENTbio develops a platform/technology to identify antigen-specific T cells (immune cells) that can be used for cancer therapy, autoimmunity, and more.</p>
  <div class="col-links abs"><h4>Quick Links</h4><ul><li>About Us</li><li>Stories</li><li>Advantage</li><li>Careers</li><li>Investors</li></ul></div>
  <div class="col-contact abs"><h4>Contact Info</h4><ul><li><span class="ficon"></span>+1 (555) 014-2290</li><li><span class="ficon"></span>hello@vorentbio.com</li><li><span class="ficon"></span>vorentbio.com</li></ul></div>
  <div class="col-follow abs"><h4>Follow Us</h4><ul><li><span class="ficon"></span>Newsfeed</li><li><span class="ficon"></span>Gallery</li><li><span class="ficon"></span>Microblog</li></ul></div>
  <div class="col-news abs"><h4>Newsletter Signup</h4><div class="news-input">Email</div><div class="news-btn">Subscribe</div></div>
  <div class="foot-bottom abs"><span>© 2025 VORENTbio All rights reserved.</span><div><span>Company</span><span>Privacy Policy</span><span>Terms and Conditions</span></div></div>
</footer>

</body>
</html>
```